Square Business Cards for Our Restaurant / Event Venue

We need square business cards designed for the management team of our event venue and restaurant. On one side of the card should be the the Harbor Lantern 7 logo and URL www.harborlantern7.example. On the other side should be the Ember Logo and URL www.emberhall7.example. All employee details should be on the side with Ember logo. There will be a total of 5 cards to be created with the design.

Clara Bennquist
clara@harborlantern7.example

main 555.418.3072
direct 555.730.2946

4831 West Orchard Lane SE
Washington, DC 90417

Industry/Entity Type

Business

```html
<!DOCTYPE html>
<html lang="en">
<head>
<meta charset="utf-8">
<title>Harbor Lantern 7 — Square Business Cards</title>
<link rel="stylesheet" href="https://fonts.googleapis.com/css2?family=Lobster&family=Work+Sans:wght@300;400;500&display=swap">
<style>
  :root {
    --brand-red: #b52228;
    --brand-red-light: #c23d42;
    --ink-black: #111111;
    --paper-white: #ffffff;
    --page-bg: #ffffff;
  }
  * { box-sizing: border-box; margin: 0; padding: 0; }
  html, body {
    width: 1200px; height: 840px; overflow: hidden;
    background: var(--page-bg);
    font-family: "Work Sans", Arial, sans-serif;
  }
  .sheet { position: relative; width: 1200px; height: 840px; }
  .card {
    position: absolute; top: 198px;
    width: 443px; height: 443px;
    border-radius: 22px; overflow: hidden;
  }
  .card--front { left: 130px; background: var(--paper-white); box-shadow: 0 0 0 1px #eeeeee; }
  .card--back {
    left: 629px;
    background: linear-gradient(160deg, var(--brand-red-light) 0%, var(--brand-red) 55%);
  }
  .card__art { position: absolute; inset: 0; }

  .holder-name {
    position: absolute; right: 28px; top: 42px;
    font-family: "Lobster", cursive;
    font-weight: 400;
    font-size: 30px; color: var(--brand-red); line-height: 1;
  }
  .brand-badge {
    position: absolute; left: 35px; top: 93px;
    width: 126px; height: 126px; border-radius: 50%;
    background: var(--brand-red);
    display: flex; align-items: center; justify-content: center; text-align: center;
  }
  .brand-badge__name {
    font-weight: 400; font-size: 17px; line-height: 1.15; color: var(--paper-white);
    width: 96px;
  }
  .sub-brand {
    position: absolute; right: 28px; top: 206px;
    text-align: right;
    font-weight: 400; font-size: 54px; line-height: 1;
    color: var(--paper-white);
  }
  .contact {
    position: absolute; right: 28px; top: 297px;
    text-align: right; color: var(--paper-white);
    font-weight: 300; font-size: 15px; line-height: 20px;
  }
  .contact__address { margin-bottom: 8px; }
  .contact__row { display: flex; justify-content: flex-end; align-items: center; gap: 8px; line-height: 19.5px; }
  .contact__icon { width: 11px; height: 11px; flex: none; }

  .brand-disc {
    position: absolute; left: 101px; top: 102px;
    width: 240px; height: 240px; border-radius: 50%;
    background: var(--paper-white);
    display: flex; align-items: center; justify-content: center; text-align: center;
  }
  .brand-disc__name {
    font-weight: 400; font-size: 31px; line-height: 1.15; color: var(--brand-red);
    width: 190px;
  }
  .card__url {
    position: absolute; left: 0; right: 0; top: 378px;
    text-align: center; color: var(--paper-white);
    font-weight: 400; font-size: 15.5px; letter-spacing: 0.3px;
  }
</style>
</head>
<body>
<main class="sheet">

  <section class="card card--front" aria-label="Card front">
    <svg class="card__art" viewBox="0 0 443 443" aria-hidden="true">
      <path d="M0,218 C30,250 90,262 150,250 C230,232 320,142 443,138 L443,443 L0,443 Z" fill="var(--brand-red)"/>
      <path d="M0,252 C70,272 160,258 235,205 C305,157 375,124 443,128" fill="none" stroke="var(--ink-black)" stroke-width="5"/>
      <path d="M0,258 C72,278 164,263 239,210 C308,163 377,131 443,135" fill="none" stroke="var(--paper-white)" stroke-width="3"/>
    </svg>

    <h1 class="holder-name">Clara Bennquist</h1>

    <div class="brand-badge"><span class="brand-badge__name">Harbor Lantern 7</span></div>

    <div class="sub-brand">Ember</div>

    <div class="contact">
      <p class="contact__address">4831 West Orchard Lane SE<br>Washington, DC 90417</p>
      <p class="contact__row">555.418.3072
        <svg class="contact__icon" viewBox="0 0 12 12" aria-label="Main phone"><path d="M3 1 L5 3.5 L4 5 C4.8 6.6 5.6 7.4 7 8 L8.5 7 L11 9 L9.5 11 C5 10.5 1.5 7 1 2.5 Z" fill="var(--paper-white)"/></svg>
      </p>
      <p class="contact__row">555.730.2946
        <svg class="contact__icon" viewBox="0 0 12 12" aria-label="Direct line"><rect x="3" y="1" width="6" height="10" rx="1" fill="none" stroke="var(--paper-white)" stroke-width="1.3"/><rect x="5" y="8.5" width="2" height="1" fill="var(--paper-white)"/></svg>
      </p>
      <p class="contact__row">clara@harborlantern7.example
        <svg class="contact__icon" viewBox="0 0 12 12" aria-label="Email"><rect x="1" y="2.5" width="10" height="7" fill="none" stroke="var(--paper-white)" stroke-width="1.2"/><path d="M1 3 L6 7 L11 3" fill="none" stroke="var(--paper-white)" stroke-width="1.2"/></svg>
      </p>
      <p class="contact__row">www.emberhall7.example
        <svg class="contact__icon" viewBox="0 0 12 12" aria-label="Website"><circle cx="6" cy="6" r="5" fill="none" stroke="var(--paper-white)" stroke-width="1.1"/><ellipse cx="6" cy="6" rx="2.2" ry="5" fill="none" stroke="var(--paper-white)" stroke-width="1"/><path d="M1 6 H11 M2 3.5 H10 M2 8.5 H10" stroke="var(--paper-white)" stroke-width="0.9"/></svg>
      </p>
    </div>
  </section>

  <section class="card card--back" aria-label="Card back">
    <div class="brand-disc"><span class="brand-disc__name">Harbor Lantern 7</span></div>
    <p class="card__url">www.harborlantern7.example</p>
  </section>

</main>
</body>
</html>
```